Business card design needed

I need a business card for my new Food & Lifestyle Coaching business - "Bloomwell Food & Lifestlye Coaching"

i already have a logo and would like to have that incorporated into the business card, obviously.

i would like a design that says "fresh" and "funky" - my target market is female, aged 20-45 so i want something that will stand out to them when they see it.

My "Company Colour" is Apple Green
Updates

Thankyou to everyone who has submitted a design for my project. At this stage i have quite a large number of designs to chose from and with only a short time until my project closes i am focusing now on chosing from those i have already shortlisted so am unfortunately not considering any new desings.

Thankyou again for your interest in my project.

Target Market(s)

Female, Health Conscious (or looking to improve their health/lifestyle), aged between 20-45

Industry/Entity Type

Business

Contact Information for Business Card

Tessa Harlow
Ph: 0438215790
Email: hellobloom@quarlmail.com

Requirements
Must have
• Must include my existing Logo
Nice to have
• Would be nice to incoirporate and appointment card on the back

```html
<!DOCTYPE html>
<html lang="en">
<head>
<meta charset="utf-8">
<title>Bloomwell Food &amp; Lifestlye Coaching – Business Card</title>
<link href="https://fonts.googleapis.com/css2?family=Montserrat:wght@400;500&display=swap" rel="stylesheet">
<style>
  :root {
    --apple-green: #a6cf39;
    --leaf-tint: #d3e79b;
    --paper: #ffffff;
    --ink-grey: #7a7a7a;
    --rule-grey: #b5b5b5;
    --stage: #ffffff;
  }
  * { margin: 0; padding: 0; box-sizing: border-box; }
  html, body {
    width: 1200px; height: 1000px; overflow: hidden;
    background: var(--stage);
    font-family: "Montserrat", Arial, sans-serif;
  }
  .canvas { position: relative; width: 1200px; height: 1000px; }

  .card {
    position: absolute;
    background: var(--paper);
    overflow: hidden;
    box-shadow: 0 6px 14px rgba(0,0,0,0.12);
  }
  .card--front { left: 315px; top: 177px; width: 572px; height: 321px; background: var(--apple-green); }
  .card--back  { left: 312px; top: 521px; width: 578px; height: 327px; }

  .front-art { position: absolute; inset: 0; width: 572px; height: 321px; }

  .brand {
    position: absolute; right: 65px; top: 36px;
    color: var(--paper); font-weight: 400; text-align: right; line-height: 1;
  }
  .brand__name { font-size: 40px; letter-spacing: 0.5px; }
  .brand__tagline { font-size: 8px; margin-top: 6px; letter-spacing: 0.2px; }

  .contact {
    position: absolute; right: 62px; top: 182px;
    text-align: right; color: var(--ink-grey);
  }
  .contact__name { font-size: 18px; letter-spacing: 1.2px; font-weight: 400; text-transform: uppercase; }
  .contact__phone { font-size: 19px; font-weight: 500; letter-spacing: 0.6px; margin-top: 25px; margin-right: 7px; }
  .contact__email { font-size: 15.5px; font-weight: 400; letter-spacing: 0.3px; margin-top: 6px; }

  .appointment__label {
    position: absolute; left: 55px; top: 61px;
    font-size: 18px; letter-spacing: 1.1px; color: var(--ink-grey); font-weight: 400;
  }
  .appointment__line {
    position: absolute; left: 55px; top: 133px; width: 331px;
    border-top: 2px dotted var(--rule-grey);
  }

  .back-mark {
    position: absolute; right: 40px; top: 238px;
    display: flex; align-items: center; gap: 8px;
    color: var(--apple-green); font-size: 20px; font-weight: 400;
  }
  .back-mark__dot { width: 14px; height: 14px; border-radius: 50%; background: var(--apple-green); }
</style>
</head>
<body>
<main class="canvas">

  <section class="card card--front" aria-label="Business card front">
    <svg class="front-art" viewBox="0 0 572 321" aria-hidden="false">
      <ellipse role="img" aria-label="Faint leaf decoration in pale green"
               cx="105" cy="200" rx="140" ry="135" fill="var(--leaf-tint)" opacity="0.9"/>
      <path class="front-art__sweep" d="M145 321 C 230 190, 380 130, 572 155 L572 321 Z" fill="var(--paper)"/>
    </svg>

    <div class="brand">
      <div class="brand__name">Bloomwell</div>
      <div class="brand__tagline">Food &amp; Lifestlye Coaching</div>
    </div>

    <div class="contact">
      <p class="contact__name">Tessa Harlow</p>
      <p class="contact__phone">0438215790</p>
      <p class="contact__email">hellobloom@quarlmail.com</p>
    </div>
  </section>

  <section class="card card--back" aria-label="Appointment card back">
    <p class="appointment__label">YOUR NEXT APPOINTMENT:</p>
    <div class="appointment__line"></div>
    <div class="back-mark">
      <span class="back-mark__dot"></span>
      <span class="back-mark__name">Bloomwell</span>
    </div>
  </section>

</main>
</body>
</html>
```